The Hidden Scroll Of Verse

We need a poster design for an indie movie
Synopsis
Brooklyn New York 1988, the golden age of rap. The young delphine Hargrove must seek and find The hidden scroll of verse in order to have the powers to win back her fathers chain and return home before her mother discovers its gone.
The story is heavily influence by the sorcerer of Quell and the Marblers
And I am looking for a poster that will focus more on the book
I like the poster designer of the silent harbor

I am looking for basically the book to be the center part if not the whole design an old leather book with gold trim that says
The Lost
Book
Of
Rap
maybe the image of the cast grabbing for it, or Just by itself on a marble pedestal
Updates

Project Deadline Extended
Reason: I am still looking for something that represent the look and feel of the story I am open to any ideas Thanks

Target Market(s)

Old school hip hop fans, young people 14-21

Industry/Entity Type

Movie

Requirements
Must have
• The title
The hidden scroll of verse
Chatterbox page /thehiddenscrollofverse
Website thehiddenscrollofverse .com

```html
<!DOCTYPE html>
<html lang="en">
<head>
<meta charset="utf-8">
<title>The Hidden Scroll Of Verse — Poster</title>
<link rel="stylesheet" href="https://fonts.googleapis.com/css2?family=Josefin+Sans:wght@300&family=Share+Tech+Mono&display=swap">
<style>
  :root {
    --stage: #d9d9d9;
    --leather-dark: #0c0b09;
    --leather-mid: #2a2418;
    --leather-edge: #6b4a24;
    --gold-light: #ffe58a;
    --gold: #e0a526;
    --gold-deep: #9a6410;
    --caption: #cfcfcf;
  }
  * { margin: 0; padding: 0; box-sizing: border-box; }
  html, body { width: 1200px; height: 531px; overflow: hidden; }
  body { background: var(--stage); }

  .poster {
    position: absolute;
    left: 395px;
    top: 0;
    width: 410px;
    height: 531px;
    overflow: hidden;
  }
  .poster__leather {
    position: absolute;
    inset: 0;
    background:
      radial-gradient(ellipse at 45% 55%, var(--leather-mid) 0%, var(--leather-dark) 70%),
      var(--leather-dark);
  }
  .poster__spine-wear {
    position: absolute;
    left: 0; top: 0; bottom: 0;
    width: 18px;
    background: linear-gradient(90deg, var(--leather-edge), transparent);
    opacity: .6;
  }
  .poster__chains {
    position: absolute;
    top: 0; bottom: 0;
    right: 0;
    width: 78px;
    background: linear-gradient(90deg, rgba(154,100,16,0) 0%, var(--gold-deep) 30%, var(--gold) 55%, var(--gold-light) 70%, var(--gold-deep) 100%);
    opacity: .85;
  }

  .title {
    position: absolute;
    left: 18px;
    top: 34px;
    width: 310px;
    font-family: "Josefin Sans", sans-serif;
    font-weight: 300;
    font-size: 68px;
    line-height: 76px;
    letter-spacing: 1px;
    text-transform: uppercase;
    color: var(--gold);
  }
  .title__line { display: block; white-space: nowrap; }

  .contact {
    position: absolute;
    left: 0;
    right: 60px;
    bottom: 22px;
    text-align: center;
    font-family: "Share Tech Mono", monospace;
    font-size: 8.5px;
    letter-spacing: 3.2px;
    text-transform: uppercase;
    color: var(--caption);
    line-height: 2.1;
  }
</style>
</head>
<body>
  <main class="poster">
    <div class="poster__leather" role="img" aria-label="Worn dark leather book cover texture"></div>
    <div class="poster__spine-wear"></div>
    <div class="poster__chains" role="img" aria-label="Hanging gold chains along the right edge"></div>

    <h1 class="title">
      <span class="title__line">The</span>
      <span class="title__line">Hidden</span>
      <span class="title__line">Scroll</span>
      <span class="title__line">Of</span>
      <span class="title__line">Verse</span>
    </h1>

    <p class="contact">
      <span class="contact__line">Chatterbox page /thehiddenscrollofverse</span><br>
      <span class="contact__line">Website thehiddenscrollofverse .com</span>
    </p>
  </main>
</body>
</html>
```